Packaging Design New Cosmetics Range

Small Establish online Beauty company is expanding it's product range into Serums, Sprays and Creams . We are looking for a new fresh packaging design for this launch.
We only use products that are Organic , Not Tested on Animals and Natural products
We would be interested in viewing a White Design , Black design and a designer choice of colors .
First Products are
Rose Water in 100ml glass bottle with box
and a set of 3 Face Serums Vit C , Retinol and Hyaluronic in 30ml Glass bottle = Box
Scrubs and creams will launch later in Q1 2020 however would like a similar feel across all products
Target Market(s)
SEA / US Markets
Industry/Entity Type
Cosmetics
Colors
Designer to choose colors to be used in the design.
Requirements
Must have
- Space Allocated for Product Use and Bar Codes on Box
Nice to have
- Organic , Not tested on animal Logo's

```html
<!DOCTYPE html>
<html lang="en">
<head>
<meta charset="utf-8">
<title>Velora Serum Label</title>
<link href="https://fonts.googleapis.com/css2?family=Open+Sans:wght@300;400;700&display=swap" rel="stylesheet">
<style>
  :root {
    --canvas: #f4f4f4;
    --label: #4b4b4b;
    --label-deep: #3f3f3f;
    --band: #5a5a5a;
    --band-line: #6e6e6e;
    --ink: #e6e6e6;
    --ink-strong: #ffffff;
  }
  * { margin: 0; padding: 0; box-sizing: border-box; }
  html, body {
    width: 1200px;
    height: 1000px;
    overflow: hidden;
    background: var(--canvas);
    font-family: "Open Sans", sans-serif;
  }
  .canvas {
    width: 1200px;
    height: 1000px;
    display: flex;
    justify-content: center;
    align-items: center;
    gap: 40px;
  }
  .label {
    position: relative;
    width: 440px;
    height: 660px;
    background: linear-gradient(180deg, var(--label) 0%, var(--label-deep) 100%);
    border-radius: 6px;
    overflow: hidden;
  }
  .key-band {
    position: absolute;
    left: 0;
    right: 0;
    height: 36px;
    background: var(--band);
    border-top: 2px solid var(--band-line);
    border-bottom: 2px solid var(--band-line);
  }
  .key-band--top { top: 70px; }
  .key-band--bottom { bottom: 70px; }

  .front__brand {
    position: absolute;
    top: 0; left: 0; right: 0; bottom: 0;
    display: flex;
    flex-direction: column;
    align-items: center;
    justify-content: center;
    gap: 18px;
  }
  .brand-mark {
    width: 22px;
    height: 22px;
    border-radius: 50%;
    background: var(--ink-strong);
  }
  .brand-name {
    font-weight: 300;
    font-size: 84px;
    letter-spacing: 1px;
    color: var(--ink-strong);
    line-height: 1;
  }

  .back__copy {
    position: absolute;
    top: 136px;
    left: 36px;
    right: 36px;
    color: var(--ink);
  }
  .back__title {
    font-weight: 700;
    font-size: 22px;
    margin-bottom: 6px;
    color: var(--ink-strong);
  }
  .back__text {
    font-weight: 400;
    font-size: 18px;
    line-height: 1.3;
  }
</style>
</head>
<body>
  <main class="canvas">
    <section class="label label--front">
      <div class="key-band key-band--top" role="img" aria-label="Greek key border pattern"></div>
      <div class="front__brand">
        <span class="brand-mark"></span>
        <span class="brand-name">velora</span>
      </div>
      <div class="key-band key-band--bottom" role="img" aria-label="Greek key border pattern"></div>
    </section>

    <section class="label label--back">
      <div class="key-band key-band--top" role="img" aria-label="Greek key border pattern"></div>
      <div class="back__copy">
        <h2 class="back__title">Organic</h2>
        <p class="back__text">It is a long established fact that a reader will be distracted by the readable content of a page when looking at its layout. The point of using Lorem Ipsum is that it has a more-or-less normal distribution of letters, as opposed to using 'Content here, content here', making it look like readable English. Many desktop publishing packages and web page editors now use Lorem Ipsum as their default model text, and a search for 'lorem ipsum' will uncover many web sites still in their infancy. Various versions have evolved over the years.</p>
      </div>
      <div class="key-band key-band--bottom" role="img" aria-label="Greek key border pattern"></div>
    </section>
  </main>
</body>
</html>
```